Larkmont Business Card Design Project

Double side card , just the logo on oxford white background on one side , and the rest of the information on the other side..
the company name is : Larkmont International General Trading LLC.
logo is already attached
the card to show in the info side: company name, employee name and position (job title) phone number, fax number, email address, P.O. box, Location (city and country)
deadline is already extended 4 all to have more time... thanks

```html
<!DOCTYPE html>
<html lang="en">
<head>
<meta charset="utf-8">
<title>Larkmont International – Business Card</title>
<link rel="stylesheet" href="https://fonts.googleapis.com/css2?family=Open+Sans:wght@400;600;700&display=swap">
<style>
  :root {
    --stage: #e4e5e7;
    --card: #fdfdfb;
    --ink-grey: #4a4c50;
    --ink-blue: #2f63a8;
    --muted: #5a5c60;
    --shadow: rgba(0, 0, 0, 0.18);
  }
  * { box-sizing: border-box; margin: 0; padding: 0; }
  html, body {
    width: 1200px; height: 800px; overflow: hidden;
    background: var(--stage);
    font-family: "Open Sans", Arial, sans-serif;
  }
  .stage {
    width: 1200px; height: 800px;
    display: flex; align-items: center; justify-content: center; gap: 60px;
  }
  .card {
    position: relative;
    width: 525px; height: 300px;
    background: var(--card);
    box-shadow: 0 10px 28px var(--shadow);
  }
  /* Logo side */
  .card--front { display: flex; align-items: center; justify-content: center; }
  .brand {
    display: flex; align-items: center; gap: 14px;
    color: var(--ink-grey);
    font-weight: 600; letter-spacing: 0.06em;
  }
  .brand__dot { width: 16px; height: 16px; border-radius: 50%; background: var(--ink-blue); }
  .card--front .brand__name { font-size: 40px; }

  /* Info side */
  .card--back { padding: 30px 36px; }
  .card--back .brand__name { font-size: 24px; }
  .person { margin-top: 16px; }
  .person__name { font-size: 19px; color: var(--ink-blue); font-weight: 400; }
  .person__name strong { font-weight: 700; }
  .person__title { font-size: 10px; color: var(--muted); letter-spacing: 0.05em; text-transform: uppercase; margin-top: 1px; }
  .contact { list-style: none; margin-top: 14px; }
  .contact__item {
    display: flex; align-items: flex-start; gap: 10px;
    font-size: 12.5px; color: var(--ink-blue); line-height: 1.35;
    margin-bottom: 6px;
  }
  .contact__item--address { margin-top: 12px; }
  .contact__icon { width: 13px; height: 13px; flex: none; margin-top: 2px; fill: var(--ink-grey); }
  .legal-name {
    position: absolute; right: 34px; bottom: 28px;
    font-size: 12px; color: var(--muted);
  }
</style>
</head>
<body>
<main class="stage">
  <section class="card card--front" aria-label="Card logo side">
    <div class="brand">
      <span class="brand__dot" aria-hidden="true"></span>
      <span class="brand__name">Larkmont Int.</span>
    </div>
  </section>

  <section class="card card--back" aria-label="Card information side">
    <div class="brand">
      <span class="brand__name">Larkmont Int.</span>
    </div>
    <div class="person">
      <p class="person__name">Daniel <strong>Reyes</strong></p>
      <p class="person__title">Founder</p>
    </div>
    <ul class="contact">
      <li class="contact__item">
        <svg class="contact__icon" viewBox="0 0 16 16" aria-hidden="true"><path d="M3.5 1 6 4 4.6 5.8c.9 2 2.6 3.7 4.6 4.6L11 9l3 2.5-1.5 2.8C7 14 2 9 1.7 3.5Z"/></svg>
        <span>+ 1 555 208 3190</span>
      </li>
      <li class="contact__item">
        <svg class="contact__icon" viewBox="0 0 16 16" aria-hidden="true"><path d="M4 1h8v4H4Z M1 6h14v7h-3v2H4v-2H1Z M5 10v4h6v-4Z" fill-rule="evenodd"/></svg>
        <span>+ 1 555 208 3146</span>
      </li>
      <li class="contact__item">
        <svg class="contact__icon" viewBox="0 0 16 16" aria-hidden="true"><path d="M1 3h14v10H1Zm1.5 1.2v.4L8 8.6l5.5-4v-.4ZM2.5 6.2v5.6h11V6.2L8 10.2Z" fill-rule="evenodd"/></svg>
        <span>daniel@larkmontint.com</span>
      </li>
      <li class="contact__item contact__item--address">
        <svg class="contact__icon" viewBox="0 0 16 16" aria-hidden="true"><path d="M8 1 1 7.5h2V15h4v-4h2v4h4V7.5h2Z"/></svg>
        <span>48 Harlow Street Milbury<br>OR, 97406</span>
      </li>
    </ul>
    <p class="legal-name">Larkmont International General Trading LLC.</p>
  </section>
</main>
</body>
</html>
```